Bright Fern Custom Homes business card. Double sided. Modern. professional

Bright Fern Custom Homes
contemporary modern design with our logo /
Double sided with all our contact information
Use same Green colors as in our Logo. Contemporary logo that grabs your attention. Visually pleasing and balanced. Easy to read, and Vibrant. Would love an option for rounded edges. Embossed logo would be amazing.
Contact Information for Business Card
Dana Welk Owner / General Contractor Bright Fern Custom Homes p: 704.552.1830 m: 912.648.2071 e: brightferncustomhomes@mailbox.example w: www.brightferncustomhomes.example 218 Pryor Meadow Lane Cedar Hollow, NC 28615

```html
<!DOCTYPE html>
<html lang="en">
<head>
<meta charset="utf-8">
<title>Bright Fern Custom Homes – Business Card</title>
<link rel="stylesheet" href="https://fonts.googleapis.com/css2?family=Cinzel:wght@400;500&family=Lato:wght@400&display=swap">
<style>
  :root {
    --stage: #e6e7e4;
    --fern: #61753a;
    --fern-emboss: #6c8142;
    --leaf: #5f7a35;
    --ink: #1f1f1f;
    --muted: #555555;
    --paper: #ffffff;
  }
  * { box-sizing: border-box; margin: 0; padding: 0; }
  html, body { width: 1200px; height: 801px; overflow: hidden; }
  body {
    background: var(--stage);
    display: flex;
    align-items: center;
    justify-content: center;
    gap: 40px;
    font-family: "Lato", sans-serif;
  }
  .card {
    position: relative;
    width: 540px;
    height: 309px;
    border-radius: 20px;
    overflow: hidden;
    box-shadow: 0 6px 18px rgba(0,0,0,.18);
  }
  .card--back {
    background: var(--fern);
    display: flex;
    align-items: center;
    justify-content: center;
    gap: 14px;
  }
  .back-mark {
    width: 22px; height: 22px;
    border-radius: 50%;
    background: var(--fern-emboss);
  }
  .back-wordmark {
    font-family: "Cinzel", serif;
    font-weight: 400;
    font-size: 28px;
    letter-spacing: 1px;
    color: var(--fern-emboss);
  }
  .card--front { background: var(--paper); }
  .holder {
    position: absolute;
    top: 32px; right: 30px;
    text-align: right;
  }
  .holder-name {
    font-family: "Cinzel", serif;
    font-weight: 500;
    font-size: 24px;
    color: var(--fern);
    line-height: 1.1;
  }
  .holder-role {
    font-size: 13px;
    color: var(--muted);
  }
  .wordmark {
    position: absolute;
    top: 104px; left: 34px;
    font-family: "Cinzel", serif;
    font-weight: 400;
    font-size: 19px;
    color: var(--fern);
    letter-spacing: .5px;
  }
  .emblem {
    position: absolute;
    top: 98px; right: 0;
    width: 170px; height: 128px;
    border-radius: 40px 0 0 20px;
    background: linear-gradient(135deg, #4f6a2a 0%, var(--leaf) 55%, #7a9a42 100%);
  }
  .address {
    position: absolute;
    top: 154px; left: 40px;
    font-size: 13px;
    line-height: 1.45;
    color: var(--ink);
  }
  .contacts {
    position: absolute;
    top: 206px; left: 40px;
    list-style: none;
    font-size: 13px;
    line-height: 1.5;
    color: var(--ink);
  }
  .contacts li { display: flex; align-items: center; gap: 8px; }
  .contacts svg { width: 12px; height: 12px; fill: var(--fern); flex: none; }
</style>
</head>
<body>
  <section class="card card--back" aria-label="Card back">
    <span class="back-mark"></span>
    <span class="back-wordmark">Bright Fern Custom Homes</span>
  </section>

  <section class="card card--front" aria-label="Card front">
    <div class="holder">
      <p class="holder-name">DANA WELK</p>
      <p class="holder-role">Owner / General Contractor</p>
    </div>

    <p class="wordmark">Bright Fern Custom Homes</p>

    <div class="emblem" role="img" aria-label="Green tree and house illustration"></div>

    <p class="address">218 Pryor Meadow Lane<br>Cedar Hollow, NC 28615</p>

    <ul class="contacts">
      <li>
        <svg viewBox="0 0 24 24"><path d="M6.6 10.8a15 15 0 0 0 6.6 6.6l2.2-2.2c.3-.3.7-.4 1-.2 1.1.4 2.300.6 3.600.6.6 0 1 .4 1 1V20c0 .6-.4 1-1 1A17 17 0 0 1 3 4c0-.6.4-1 1-1h3.5c.6 0 1 .4 1 1 0 1.3.2 2.5.6 3.6.1.3 0 .7-.2 1z"/></svg>
        704.552.1830
      </li>
      <li>
        <svg viewBox="0 0 24 24"><path d="M7 1h10a2 2 0 0 1 2 2v18a2 2 0 0 1-2 2H7a2 2 0 0 1-2-2V3a2 2 0 0 1 2-2zm0 3v14h10V4zm5 15.5a1.2 1.2 0 1 0 0 2.4 1.2 1.2 0 0 0 0-2.4z"/></svg>
        912.648.2071
      </li>
      <li>
        <svg viewBox="0 0 24 24"><path d="M2 5h20v14H2zm2 2v.5l8 5 8-5V7zm0 2.8V17h16V9.8l-8 5z"/></svg>
        brightferncustomhomes@mailbox.example
      </li>
      <li>
        <svg viewBox="0 0 24 24"><path d="M12 2a10 10 0 1 0 0 20 10 10 0 0 0 0-20zm6.9 6h-2.9a15 15 0 0 0-1.4-3.6A8 8 0 0 1 18.9 8zM12 4c.8 1.2 1.5 2.5 1.9 4h-3.8c.4-1.5 1.1-2.8 1.9-4zM4.3 14a8 8 0 0 1 0-4h3.4a16 16 0 0 0 0 4zm.8 2h2.9c.3 1.3.8 2.5 1.4 3.6A8 8 0 0 1 5.1 16zM8 8H5.1a8 8 0 0 1 4.3-3.6C8.8 5.5 8.3 6.7 8 8zm4 12c-.8-1.2-1.5-2.5-1.9-4h3.8c-.4 1.5-1.1 2.8-1.9 4zm2.3-6H9.7a14 14 0 0 1 0-4h4.6a14 14 0 0 1 0 4zm.3 5.6c.6-1.1 1.1-2.3 1.4-3.6h2.9a8 8 0 0 1-4.3 3.6zm1.7-5.6a16 16 0 0 0 0-4h3.4a8 8 0 0 1 0 4z"/></svg>
        www.brightferncustomhomes.example
      </li>
    </ul>
  </section>
</body>
</html>
```